I need a letterhead for a newsletter that will go out quarterly to the dentists of the 18th district. It is called "The Cobalt Bulletin" We are in Amarillo TX and have this landmark in the photo as our most prominent feature. If it could be used, that would be cool.
This is a professional organization newsletter so the letterhead should be somewhat professional.

Target Market(s)

Dentists

Industry/Entity Type

Dental

Font styles to use
Serif

Colors

Designer to choose only greyscale colors for use in the design.

Requirements
Must have
• I want the title of "The Cobalt Bulletin" to be the on top with the phrase "Brookmere Valley Dental Guild" written underneath.
Nice to have
• the photo incorporated could be incorporated in black and white or color along the bottom of the letterhead or with the title inside the photo.
Should not have
• I don't want it to be cartoony. I want it to be stylish and elegant and professional.

```html
<!DOCTYPE html>
<html lang="en">
<head>
<meta charset="utf-8">
<title>The Cobalt Bulletin — Letterhead</title>
<link href="https://fonts.googleapis.com/css2?family=Cinzel:wght@400;600&family=Didact+Gothic&family=Lato:wght@400&display=swap" rel="stylesheet">
<style>
  :root {
    --backdrop: #d6e0f2;
    --paper: #ffffff;
    --cobalt: #0a7cc4;
    --ink: #3a3a3a;
    --ink-dark: #1f1f1f;
    --on-cobalt: #ffffff;
    --photo-sky: #2a5fb0;
    --photo-rock: #c85a2a;
  }
  * { margin: 0; padding: 0; box-sizing: border-box; }
  html, body {
    width: 1200px; height: 898px; overflow: hidden;
    background: var(--backdrop);
  }
  .canvas {
    position: relative; width: 1200px; height: 898px;
  }
  .letterhead {
    position: absolute; left: 296px; top: 19px;
    width: 608px; height: 860px;
    background: var(--paper);
    box-shadow: 0 6px 24px rgba(40, 60, 100, 0.18);
    overflow: hidden;
  }
  .masthead {
    position: absolute; left: 190px; top: 0;
    width: 250px; height: 232px;
    background: var(--cobalt);
    border-radius: 0 0 22px 22px;
    text-align: center;
  }
  .masthead-photo {
    position: absolute; left: 32px; top: 26px;
    width: 186px; height: 136px;
    border: 3px solid var(--on-cobalt);
    border-radius: 20px;
    background: linear-gradient(160deg, var(--photo-sky) 0%, #6f9bd6 38%, var(--photo-rock) 62%, #8a3818 100%);
  }
  .masthead-title {
    position: absolute; left: 0; right: 0; top: 170px;
    font-family: "Cinzel", serif; font-weight: 600;
    font-size: 21px; color: var(--on-cobalt); letter-spacing: 0.5px;
  }
  .masthead-subtitle {
    position: absolute; left: 0; right: 0; top: 202px;
    font-family: "Cinzel", serif; font-weight: 400;
    font-size: 9.5px; color: var(--on-cobalt); letter-spacing: 0.4px;
  }
  .letter-body {
    position: absolute; left: 74px; top: 330px; width: 460px;
    font-family: "Didact Gothic", sans-serif;
    font-size: 11.5px; line-height: 19px; color: var(--ink);
    text-align: justify;
  }
  .salutation { margin-bottom: 18px; }
  .letter-body p.paragraph { margin-bottom: 22px; }
  .signature-name {
    font-size: 17px; color: var(--ink); margin-top: 6px; text-align: left;
  }
  .signature-role { font-size: 10.5px; text-align: left; }
  .footer-address {
    position: absolute; right: 40px; top: 744px;
    font-family: "Lato", sans-serif; font-size: 11px; color: var(--ink-dark);
  }
  .footer-band {
    position: absolute; left: 0; bottom: 0; width: 608px; height: 92px;
  }
  .footer-contacts {
    position: absolute; left: 56px; right: 30px; bottom: 26px;
    display: flex; justify-content: space-between; align-items: center;
    font-family: "Lato", sans-serif; font-size: 9.5px; color: var(--on-cobalt);
  }
  .contact-item { display: flex; align-items: center; gap: 5px; }
  .contact-item svg { width: 11px; height: 11px; fill: var(--on-cobalt); }
</style>
</head>
<body>
<div class="canvas">
  <article class="letterhead">
    <header class="masthead">
      <div class="masthead-photo" role="img" aria-label="Photograph of a red rock canyon landmark under a blue sky"></div>
      <h1 class="masthead-title">The Cobalt Bulletin</h1>
      <p class="masthead-subtitle">Brookmere Valley Dental Guild</p>
    </header>

    <section class="letter-body">
      <p class="salutation">Hello Sir/Mam,</p>
      <p class="paragraph">Lorem ipsum dolor sit amet, consectetur adipiscing elit. Donec orci purus, luctus vitae dignissim eu, iaculis sed purus. Vivamus faucibus, ipsum nec aliquet viverra, leo mauris condimentum ligula, sit amet sagittis enim ligula quis arcu. Nam egestas tortor id nisi porttitor mattis. In tortor ante, ultricies in suscipit a, tempus non massa. Vivamus et auctor mi. Fusce vel massa nulla. Phasellus nec eros mauris, et scelerisque orci. Donec malesuada orci vitae nulla accumsan porta a id massa.</p>
      <p class="paragraph">Quisque accumsan iaculis magna sit amet fringilla. Maecenas consequat, magna eget tincidunt semper, odio nibh rutrum mi, id feugiat ante nisi eu risus. Vestibulum nunc orci, rhoncus a placerat in, ultricies in mi. Cras mattis varius eros, vel fringilla nisi suscipit eget. Quisque scelerisque sagittis nulla at porttitor. Mauris a justo et tellus interdum tristique. Sed id augue vitae urna euismod commodo aliquet a quam. Pellentesque arcu velit, cursus et malesuada ut, consequat et diam. Nullam erat sem, rhoncus id ullamcorper vitae, rhoncus et arcu. In ultricies ultricies nulla.</p>
      <p class="signature-name">Elias Marlowe</p>
      <p class="signature-role">Co-Founder &amp; CEO</p>
    </section>

    <p class="footer-address">1420 Harwell Lane, Ste 210, Brookmere, TX 79101</p>

    <svg class="footer-band" viewBox="0 0 608 92" preserveAspectRatio="none" aria-hidden="true">
      <path d="M0 92 L0 52 Q0 30 28 30 L560 30 Q596 30 608 4 L608 92 Z" fill="var(--cobalt)"/>
    </svg>
    <footer class="footer-contacts">
      <span class="contact-item">
        <svg viewBox="0 0 24 24"><path d="M4 15c0-5 4-9 8-9s8 4 8 9h-4l-1-3H9l-1 3H4zm4 2h8l2 4H6z"/></svg>555.204.3187
      </span>
      <span class="contact-item">
        <svg viewBox="0 0 24 24"><path d="M4 15c0-5 4-9 8-9s8 4 8 9h-4l-1-3H9l-1 3H4zm4 2h8l2 4H6z"/></svg>555.204.3190
      </span>
      <span class="contact-item">
        <svg viewBox="0 0 24 24"><path d="M2 5h20v14H2zm2 2v1l8 5 8-5V7l-8 5z"/></svg>office@cobaltbulletin.org
      </span>
      <span class="contact-item">
        <svg viewBox="0 0 24 24"><path d="M12 2a10 10 0 1 0 0 20 10 10 0 0 0 0-20zm0 2c1.5 0 3 3 3.3 7H8.7C9 7 10.5 4 12 4zm-3.3 9h6.6c-.3 4-1.8 7-3.3 7s-3-3-3.3-7zM4 11a8 8 0 0 1 3-5.6A15 15 0 0 0 6.7 11zm0 2h2.7c.1 2.2.5 4.1 1.3 5.6A8 8 0 0 1 4 13zm13.3-2A15 15 0 0 0 17 5.4 8 8 0 0 1 20 11zm0 2H20a8 8 0 0 1-4 5.6c.8-1.5 1.2-3.4 1.3-5.6z"/></svg>www.cobaltbulletin.org
      </span>
    </footer>
  </article>
</div>
</body>
</html>
```